Shoes, Handbags and Accessories

The main business of the company are shoes and then handbags, jewellery and scarves to accessorize.

The design I am looking for is a "shabby chic" design, cursive font, perhaps with a vintage country feel to it.

Target Market(s)

Age group are more for the 25+, but more so 35+ ladies.

Industry/Entity Type

Business

Contact Information for Business Card

Lace Lane Boutique & Accessories
Marlene Toohey - P.O. Box 482, Kulbari W.A. 6281
Ph: (08) 97314426 fax: (08) 97314427 Mobile: 0419273561
Email:lacelane@brindanet.com.au
Web: www.lacelaneboutique.com.au
Like us on Chatterbook (Chatterbook logo)

Requirements
Must have
• As already described. A "faded" picture background is also another feature I like, but I don't want to create a cluttered look about the business card.
Nice to have
• Classy, stylish and comfortable shoes.

```html
<!DOCTYPE html>
<html lang="en">
<head>
<meta charset="utf-8">
<title>Lace Lane Boutique &amp; Accessories – Business Card</title>
<link rel="stylesheet" href="https://fonts.googleapis.com/css2?family=Kalam:wght@400;700&display=swap">
<style>
  :root {
    --backdrop: #2b2b2d;
    --card-white: #ffffff;
    --panel-top: #ffffff;
    --panel-bottom: #e4e4e4;
    --stripe: #2a2528;
    --ink: #1c1c1c;
    --pattern-light: #f3efe9;
    --pattern-mid: #d9c9b4;
    --pattern-warm: #c98a6a;
    --pattern-dark: #6b5a58;
  }
  * { box-sizing: border-box; margin: 0; padding: 0; }
  html, body {
    width: 1200px; height: 814px; overflow: hidden;
    background: var(--backdrop);
    font-family: "Kalam", cursive;
    color: var(--ink);
  }
  .stage {
    width: 1200px; height: 814px;
    display: flex; justify-content: center; align-items: center; gap: 60px;
  }
  .card {
    width: 360px; height: 600px;
    background: var(--card-white);
    display: flex; flex-direction: column;
    box-shadow: 0 10px 30px rgba(0,0,0,.45);
    overflow: hidden;
  }
  .shoe-pattern {
    background:
      radial-gradient(circle at 20% 30%, rgba(201,138,106,.35), transparent 40%),
      radial-gradient(circle at 75% 65%, rgba(107,90,88,.3), transparent 45%),
      linear-gradient(160deg, var(--pattern-light), var(--pattern-mid) 55%, var(--pattern-light));
  }
  .stripe { height: 14px; background: var(--stripe); flex: none; }
  .panel {
    background: linear-gradient(180deg, var(--panel-top), var(--panel-bottom));
    display: flex; flex-direction: column; align-items: center; justify-content: center;
    text-align: center;
  }

  /* front */
  .front .pattern-top { height: 68px; flex: none; }
  .front .panel { height: 160px; flex: none; }
  .front .pattern-bottom { flex: 1; }
  .brand-name {
    font-size: 33px; font-weight: 700; line-height: 1.15;
  }

  /* back */
  .back .pattern-top { height: 26px; flex: none; }
  .back .panel { height: 330px; flex: none; justify-content: flex-start; padding-top: 26px; }
  .back .pattern-bottom { flex: 1; }
  .owner-name { font-size: 23px; font-weight: 700; }
  .postal { font-size: 17px; line-height: 1.15; margin-top: 4px; }
  .online { font-size: 13.5px; line-height: 1.3; margin-top: 16px; }
  .phones { margin-top: 16px; font-size: 19px; line-height: 1.2; text-align: left; }
  .phones dt { display: inline-block; width: 30px; }
  .phones dd { display: inline; }
  .phones div { white-space: nowrap; }
  .social {
    margin-top: 14px; display: flex; align-items: center; gap: 8px;
    font-size: 19px; font-weight: 700;
  }
  .social-dot { width: 20px; height: 20px; border-radius: 50%; background: var(--ink); }
</style>
</head>
<body>
<main class="stage">
  <section class="card front" aria-label="Card front">
    <div class="shoe-pattern pattern-top" role="img" aria-label="Pattern of colourful high-heeled shoes"></div>
    <div class="stripe"></div>
    <div class="panel">
      <h1 class="brand-name">Lace Lane Boutique<br>&amp;<br>Accessories</h1>
    </div>
    <div class="stripe"></div>
    <div class="shoe-pattern pattern-bottom" role="img" aria-label="Pattern of colourful high-heeled shoes"></div>
  </section>

  <section class="card back" aria-label="Card back">
    <div class="shoe-pattern pattern-top" role="img" aria-label="Pattern of colourful high-heeled shoes"></div>
    <div class="stripe"></div>
    <div class="panel">
      <h2 class="owner-name">Marlene Toohey</h2>
      <p class="postal">P.O. Box 482,<br>Kulbari W.A. 6281</p>
      <p class="online">E: lacelane@brindanet.com.au<br>www.lacelaneboutique.com.au</p>
      <dl class="phones">
        <div><dt>F:</dt><dd>(08) 9731 4427</dd></div>
        <div><dt>P:</dt><dd>(08) 9731 4426</dd></div>
        <div><dt>M:</dt><dd>0419 273 561</dd></div>
      </dl>
      <p class="social"><span class="social-dot"></span>LIKE US ON Chatterbook</p>
    </div>
    <div class="stripe"></div>
    <div class="shoe-pattern pattern-bottom" role="img" aria-label="Pattern of colourful high-heeled shoes"></div>
  </section>
</main>
</body>
</html>
```